Gentle Kundalini Yoga with Gong Relaxation

I teach a gentle Kundalini Yoga class with Gong relaxation every Thursday morning from 8:30-10am at the Alder Crossing Congregational Church 17 Marbury Lane Alder Crossing. This class is unique in that I play the gong for an extended relaxation. Gongs are generally only found in established Yoga centers not in a small neighborhood yoga class. I am trying to grow this class from a current class size of 5 students. I would like to double the class size.
Updates
Project Deadline Extended
Reason: We had a blizzard on January 27 and 28 in the Boston area and I was too busy removing snow to tend to the postcard design-Thank you-Dolores Whitcombe
Industry/Entity Type
Church

```html
<!DOCTYPE html>
<html lang="en">
<head>
<meta charset="utf-8">
<title>Kundalini Yoga with Gong Relaxation – Postcard</title>
<link rel="stylesheet" href="https://fonts.googleapis.com/css2?family=Roboto+Condensed:wght@400;700&display=swap">
<style>
  :root {
    --page-bg: #e4e4e4;
    --card-white: #ffffff;
    --plum: #7b1f4f;
    --band-blue: #1f3f9c;
    --band-blue-dark: #173283;
    --ink-gray: #8a8a8a;
    --line-gray: #b5b5b5;
    --photo-warm: #d9893a;
    --photo-wood: #c9782e;
    --photo-floor: #2f56b8;
  }
  * { box-sizing: border-box; margin: 0; padding: 0; }
  html, body {
    width: 1200px; height: 825px; overflow: hidden;
    background: var(--page-bg);
    font-family: "Roboto Condensed", "Arial Narrow", sans-serif;
  }
  .sheet {
    width: 1200px; height: 825px;
    display: flex; align-items: center; justify-content: center; gap: 40px;
  }
  .postcard {
    position: relative;
    width: 560px; height: 385px;
    background: var(--card-white);
    box-shadow: 0 6px 18px rgba(0,0,0,0.18);
    overflow: hidden;
  }
  /* Front */
  .class-photo {
    position: absolute; inset: 0;
    background:
      linear-gradient(180deg, transparent 55%, var(--photo-floor) 100%),
      linear-gradient(120deg, var(--photo-warm) 0%, var(--photo-wood) 45%, #a8b9d8 100%);
  }
  .front-graphics { position: absolute; inset: 0; }
  .front-title { font-weight: 700; font-size: 34px; fill: #fff; }
  .front-subtitle { font-weight: 400; font-size: 21px; fill: #fff; }
  .schedule-line { font-weight: 700; font-size: 20px; fill: #fff; }
  /* Back */
  .back-layout { position: absolute; inset: 0; }
  .brand {
    position: absolute; left: 36px; top: 110px;
    display: flex; flex-direction: column; align-items: flex-start; gap: 12px;
    width: 250px;
  }
  .brand-dot {
    width: 60px; height: 60px; border-radius: 50%;
    background: var(--plum); flex: none; margin-left: 10px;
  }
  .brand-name {
    color: var(--ink-gray); font-weight: 700; line-height: 1;
  }
  .brand-name .name { display: block; font-size: 34px; }
  .brand-name .tagline { display: block; font-size: 20px; margin-top: 2px; padding-left: 20px; }
  .return-address {
    position: absolute; left: 36px; bottom: 30px;
    color: var(--ink-gray); font-size: 13px; line-height: 1.35; font-style: normal;
  }
  .divider {
    position: absolute; left: 300px; top: 40px; bottom: 40px;
    border-left: 1px solid #dcdcdc;
  }
  .stamp-box {
    position: absolute; right: 28px; top: 28px;
    width: 70px; height: 84px;
    border: 1px solid var(--line-gray);
  }
  .address-lines {
    position: absolute; left: 330px; right: 28px; top: 170px;
    display: flex; flex-direction: column; gap: 44px;
  }
  .address-lines span { display: block; border-bottom: 1px dotted var(--line-gray); }
</style>
</head>
<body>
<main class="sheet">

  <section class="postcard postcard--front" aria-label="Postcard front">
    <div class="class-photo" role="img" aria-label="Photo of a group of adults seated on blue mats in a wooden-floored studio, stretching sideways in a yoga class"></div>
    <svg class="front-graphics" viewBox="0 0 560 385" width="560" height="385">
      <polygon points="0,300 300,268 300,326 0,372" fill="var(--band-blue)"/>
      <polygon points="0,372 300,326 300,340 0,385" fill="var(--band-blue-dark)"/>
      <text class="front-title" x="20" y="318" transform="rotate(-6 20 318)">Kundalini Yoga</text>
      <text class="front-subtitle" x="44" y="342" transform="rotate(-6 44 342)">with Gong relaxation</text>
      <polygon points="300,218 560,180 560,248 306,286" fill="var(--plum)"/>
      <g transform="rotate(-8 432 240)">
        <text class="schedule-line" x="432" y="235" text-anchor="middle">Every Thursday Morning</text>
        <text class="schedule-line" x="432" y="259" text-anchor="middle">from 8:30-10am</text>
      </g>
    </svg>
  </section>

  <section class="postcard postcard--back" aria-label="Postcard back">
    <div class="back-layout">
      <div class="brand">
        <span class="brand-dot"></span>
        <p class="brand-name">
          <span class="name">Kundalini Yoga</span>
          <span class="tagline">with Gong relaxation</span>
        </p>
      </div>
      <address class="return-address">
        Alder Crossing Congregational Church<br>
        17 Marbury Lane, Alder Crossing
      </address>
      <div class="divider"></div>
      <div class="stamp-box"></div>
      <div class="address-lines">
        <span></span><span></span><span></span>
      </div>
    </div>
  </section>

</main>
</body>
</html>
```